VIRTUAL KIDS PARTIES for ages 3-10 years

I need a very urgent leaflet, that looks fun and eye catching aimed at ages 3-10 years.

Award winning, accredited, performing arts provider KMO are excited to bring you LIVE interactive drama, singing and dance parties taught by industry qualified performers that can be accessed from home.

* A chance for your child to hook up with their classmates and friends.

* An interactive hour of games, dancing and singing amongst friends as you talk, laugh and play together on screen.

* Tailor made themes, music choices and routines.

* A chance to socialise in a safe environment and celebrate that special day.

* All staff are qualified, DBS checked industry professionals and teachers.

* Flexible times to suit.

Packages start from £65 plus vat

Visit www.brightstagework.co.uk to book
Check out our online performing arts classes and interactive sessions.

Target Market(s)

Parents and children ages 3-10 years

Colors
ef3f46
ffc214
faa54b
33a6d7
87d0c7
abd037

Requirements
Must have
• Clear text that this is a service for ONLINE VIRTUAL parties

Should be upbeat, happy, bright & vibrant

Logo ( attached)

MUST LOOK PROFESSIONAL

Photo or clever art designs if designer can do this

See attached photos and leaflets for inspiration
Nice to have
• Emphasis on Dance, drama, musical theatre, singing

```html
<!DOCTYPE html>
<html lang="en">
<head>
<meta charset="utf-8">
<title>KMO Online Virtual Parties Leaflet</title>
<link rel="stylesheet" href="https://fonts.googleapis.com/css2?family=Quicksand:wght@500;600;700&family=Gochi+Hand&display=swap">
<style>
  :root {
    --stage: #c9c9c9;
    --purple-deep: #2a0b3d;
    --purple: #5b1c7a;
    --purple-light: #9b4fc4;
    --screen: #2b2b2b;
    --screen-edge: #111111;
    --pink: #e8336f;
    --yellow: #ffc214;
    --white: #ffffff;
    --red: #ef3f46;
    --orange: #faa54b;
    --blue: #33a6d7;
    --green: #abd037;
    --logo-blue: #3b3fb0;
  }
  * { margin: 0; padding: 0; box-sizing: border-box; }
  html, body { width: 1200px; height: 960px; overflow: hidden; }
  body {
    background: radial-gradient(ellipse at 50% 40%, #e6e6e6, var(--stage));
    font-family: 'Quicksand', sans-serif;
    position: relative;
  }
  .leaflet {
    position: absolute;
    left: 282px; top: 30px;
    width: 636px; height: 900px;
    overflow: hidden;
    background: radial-gradient(ellipse at 55% 60%, var(--purple-light) 0%, var(--purple) 45%, var(--purple-deep) 100%);
    box-shadow: 0 12px 30px rgba(0,0,0,0.25);
  }
  .balloons {
    position: absolute; left: 0; top: 0; width: 636px; height: 520px;
    background:
      radial-gradient(circle at 80px 60px, var(--blue) 0 70px, transparent 71px),
      radial-gradient(circle at 300px 40px, var(--red) 0 75px, transparent 76px),
      radial-gradient(circle at 470px 120px, var(--green) 0 80px, transparent 81px),
      radial-gradient(circle at 590px 40px, var(--orange) 0 70px, transparent 71px),
      radial-gradient(circle at 600px 250px, var(--red) 0 80px, transparent 81px),
      radial-gradient(circle at 590px 420px, var(--blue) 0 75px, transparent 76px),
      radial-gradient(circle at 60px 220px, var(--orange) 0 60px, transparent 61px),
      linear-gradient(180deg, #6a2a93 0%, rgba(91,28,122,0) 100%);
  }
  .brand {
    position: absolute; left: 110px; top: 40px;
    display: flex; align-items: center; gap: 10px;
  }
  .brand-dot { width: 22px; height: 22px; border-radius: 50%; background: var(--yellow); }
  .brand-name { font-weight: 700; font-size: 40px; color: var(--white); letter-spacing: 2px; }
  .screen {
    position: absolute; left: 40px; top: 160px; width: 500px; height: 320px;
    background: linear-gradient(150deg, #3a3a3a, var(--screen) 55%, #1e1e1e);
    border: 8px solid var(--screen-edge);
    border-radius: 6px;
  }
  .title {
    position: absolute; left: 40px; top: 290px; width: 500px;
    text-align: center;
    font-family: 'Gochi Hand', cursive;
    font-size: 44px; color: var(--pink); letter-spacing: 3px;
  }
  .details {
    position: absolute; left: 36px; top: 505px; width: 292px;
    font-size: 12.5px; line-height: 1.35; font-weight: 600; color: var(--white);
  }
  .intro { color: var(--yellow); text-align: center; margin-bottom: 6px; }
  .features { list-style: none; }
  .features li { padding-left: 10px; position: relative; }
  .features li::before { content: "•"; position: absolute; left: 0; }
  .call-photo {
    position: absolute; left: 420px; top: 450px; width: 220px; height: 220px;
    border-radius: 50%; border: 5px solid var(--red);
    background: radial-gradient(circle at 40% 40%, #c98a6a, #5a3a30 70%, #2a1a18);
  }
  .price {
    position: absolute; left: 330px; top: 610px; width: 180px; height: 180px;
    border-radius: 50%; border: 5px solid var(--orange);
    background: radial-gradient(circle at 50% 40%, #f4744a, var(--red));
    color: var(--white); text-align: center;
    display: flex; flex-direction: column; justify-content: center; align-items: center;
    font-weight: 600;
  }
  .price-lead { font-size: 15px; line-height: 1.2; }
  .price-amount { font-size: 54px; font-weight: 700; line-height: 1.1; }
  .price-note { font-size: 15px; }
  .booking {
    position: absolute; left: 36px; top: 810px; width: 580px;
    font-size: 17px; font-weight: 700; color: var(--yellow); line-height: 1.4;
  }
  .booking .site { color: var(--pink); }
</style>
</head>
<body>
  <main class="leaflet">
    <div class="balloons" role="img" aria-label="Colourful party balloons and confetti"></div>
    <div class="brand"><span class="brand-dot"></span><span class="brand-name">KMO</span></div>
    <div class="screen" role="img" aria-label="Cartoon children waving in video call tiles on a screen"></div>
    <h1 class="title">ONLINE VIRTUAL PARTIES</h1>
    <section class="details">
      <p class="intro">Award winning, accredited, performing arts provider KMO are excited to bring you LIVE interactive drama, singing and dance parties taught by industry qualified performers that can be accessed from home.</p>
      <ul class="features">
        <li>A chance for your child to hook up with their classmates and friends.</li>
        <li>An interactive hour of games, dancing and singing amongst friends as you talk, laugh and play together on screen.</li>
        <li>Tailor made themes, music choices and routines.</li>
        <li>A chance to socialise in a safe environment and celebrate that special day.</li>
        <li>All staff are qualified, DBS checked industry professionals and teachers.</li>
        <li>Flexible times to suit.</li>
      </ul>
    </section>
    <div class="call-photo" role="img" aria-label="Photo of children joining a party on a video call"></div>
    <div class="price">
      <span class="price-lead">Packages<br>start from</span>
      <span class="price-amount">£65</span>
      <span class="price-note">plus vat</span>
    </div>
    <p class="booking">Visit <span class="site">www.brightstagework.co.uk</span> to book<br>Check out our online performing arts classes and interactive sessions.</p>
  </main>
</body>
</html>
```